Frozen Yogurt Cup Design

We are looking for an art design for our 16 oz frozen yogurt cup for our company named, "Pinwhirl: Frozen Yogurt Adventure." The target audience for a self-served yogurt place varies from children to adults, the final design should be versatile. We are looking for a design that incorporates our logo and the colors of lime green, yellow, orange, and royal blue. The final design should be modern, clean, and playful.

Target Market(s)

Ages 0 to 100

Industry/Entity Type

Royal

Requirements
Must have
• Attached logo design (out of the two designs please use the top one)

```html
<!DOCTYPE html>
<html lang="en">
<head>
<meta charset="utf-8">
<title>Pinwhirl – Frozen Yogurt Adventure Banner</title>
<link href="https://fonts.googleapis.com/css2?family=Open+Sans:wght@700;800&display=swap" rel="stylesheet">
<style>
  :root {
    --paper: #ffffff;
    --royal-blue: #1e6fa0;
    --autumn-orange: #db8a1f;
    --rust: #b9532b;
    --leaf-light: #e39a2a;
  }
  html, body {
    margin: 0;
    padding: 0;
    overflow: hidden;
    background: var(--paper);
  }
  .banner {
    position: relative;
    width: 1200px;
    height: 257px;
    overflow: hidden;
    background: var(--paper);
    font-family: "Open Sans", Arial, sans-serif;
  }
  .banner__shapes {
    position: absolute;
    inset: 0;
  }
  .brand-name {
    position: absolute;
    left: 194px;
    top: 104px;
    margin: 0;
    font-size: 58px;
    font-weight: 800;
    line-height: 1;
    letter-spacing: -1px;
    color: var(--royal-blue);
  }
  .tagline {
    position: absolute;
    left: 598px;
    top: 97px;
    margin: 0;
    font-size: 34px;
    font-weight: 700;
    line-height: 1;
    color: var(--autumn-orange);
  }
</style>
</head>
<body>
  <main class="banner">
    <svg class="banner__shapes" width="1200" height="257" viewBox="0 0 1200 257" aria-hidden="false">
      <defs>
        <linearGradient id="autumn-leaves-tone" x1="0" y1="0" x2="1" y2="1">
          <stop offset="0" stop-color="var(--rust)"/>
          <stop offset="0.6" stop-color="var(--leaf-light)"/>
          <stop offset="1" stop-color="var(--autumn-orange)"/>
        </linearGradient>
      </defs>

      <!-- blue field -->
      <path class="field-blue" fill="var(--royal-blue)"
            d="M596,0 C572,118 522,198 412,257 L1200,257 L1200,0 Z"/>

      <!-- orange leaf curve dividing the fields -->
      <path class="divider-leaf" fill="var(--autumn-orange)"
            d="M596,0 C520,22 462,82 464,140 C466,188 448,222 412,257 C522,198 572,118 596,0 Z"/>

      <!-- autumn leaves, top left -->
      <path class="leaves-top-left" role="img" aria-label="Cluster of orange and rust maple leaves"
            fill="url(#autumn-leaves-tone)"
            d="M0,0 L150,0 C170,40 195,70 185,105 C160,140 130,170 80,190 C45,170 15,160 0,150 Z"/>

      <!-- autumn leaves, bottom right -->
      <path class="leaves-bottom-right" role="img" aria-label="Cluster of rust and orange maple leaves"
            fill="url(#autumn-leaves-tone)"
            d="M1160,30 C1185,60 1200,80 1200,100 L1200,257 L1080,257 C1070,220 1068,180 1095,150 C1110,110 1135,70 1160,30 Z"/>
    </svg>

    <h1 class="brand-name">Pinwhirl</h1>
    <p class="tagline">Frozen Yogurt Adventure</p>
  </main>
</body>
</html>
```